Velmora Skincare packaging designs

We are need to create packaging for our skincare brand. We need two designs. One for round jars which is for creams/capsules and the second will be for bottles/serums Some products will be larger in size so please ensure the packaging design will work and there isn't a lot white/empty space

Below are the names of some of our products.
Screw-On Top Jar (25 pads- 4 inches wide) - Glint Wipes I Skin Brightening Pads
Pump Bottle (2 oz) - ReVIVANT I Hyaluronic Acid + Vitamin Serum
Pump Bottle (6oz) - The Oat Rinse I Conditioning Face Cleanser
Dropper bottle (1 oz) - Quiet Glow I Hydrating Moisturizer
Cream jar (1.5 oz) - Quiet Glow I Hydrating Moisturizer
Capsules Jar (25 capsules in a jar)- Plume Drop I Moisture + Hydrating Capsules
Capsules Jar (25 capsules in a jar) - Clear Burst I Impurity Capsules

We will also need help with the packing design in terms of layout of the logo, item name, desc, and ingredients on each product.

Target Market(s)

women

Industry/Entity Type

skincare, beauty

Font styles to use
Sans Serif

Colors
E54698
E96AAD
F1A4CE
F9D9EA
FCEFF6

Requirements
Must have
• Pantone color is 2052 CP HEX #DAAFCA (218 , 175 , 202)

```html
<!DOCTYPE html>
<html lang="en">
<head>
<meta charset="utf-8">
<title>Velmora Skincare – The Oat Rinse label</title>
<link rel="stylesheet" href="https://fonts.googleapis.com/css2?family=Barlow+Condensed:wght@300;500;600&display=swap">
<style>
  :root {
    --label-white: #f7f7f7;
    --label-white-shade: #e6e6e6;
    --rose: #c2607e;
    --rose-light: #cc6d89;
    --rose-deep: #b5546f;
    --ink-light: #fbf4f6;
  }
  * { margin: 0; padding: 0; box-sizing: border-box; }
  html, body { width: 800px; height: 1200px; overflow: hidden; }
  body { font-family: "Barlow Condensed", "Arial Narrow", sans-serif; background: var(--label-white); }

  .label { position: relative; width: 800px; height: 1200px; }

  .label__top {
    position: absolute; left: 0; top: 0; width: 800px; height: 380px;
    background: linear-gradient(90deg, var(--label-white) 0%, #fdfdfd 45%, var(--label-white-shade) 100%);
  }
  .label__body {
    position: absolute; left: 0; top: 380px; width: 800px; height: 820px;
    background: linear-gradient(90deg, var(--rose-deep) 0%, var(--rose-light) 35%, var(--rose) 60%, var(--rose-deep) 100%);
  }

  .brand-name {
    position: absolute; left: 0; top: 200px; width: 800px;
    text-align: center; color: var(--rose);
    font-weight: 500; font-size: 46px; letter-spacing: 8px; text-transform: uppercase;
  }

  .product {
    position: absolute; left: 0; top: 560px; width: 800px; text-align: center; color: var(--ink-light);
  }
  .product__name {
    font-weight: 600; font-size: 62px; letter-spacing: 1px; text-transform: uppercase; line-height: 1;
  }
  .product__rule {
    width: 500px; height: 3px; margin: 20px auto 16px; background: var(--ink-light);
  }
  .product__desc {
    font-weight: 300; font-size: 28px; letter-spacing: 7px; text-transform: uppercase;
  }
  .product__size {
    position: absolute; left: 0; top: 900px; width: 800px; text-align: center; color: var(--ink-light);
    font-weight: 300; font-size: 40px; letter-spacing: 8px;
  }
</style>
</head>
<body>
  <main class="label">
    <div class="label__top" role="img" aria-label="Soft grey topographic contour pattern on white"></div>
    <div class="label__body" role="img" aria-label="Faint rose topographic contour pattern on rose pink"></div>

    <h1 class="brand-name">Velmora Skincare</h1>

    <section class="product">
      <h2 class="product__name">The Oat Rinse</h2>
      <div class="product__rule"></div>
      <p class="product__desc">Conditioning Face Cleanser</p>
    </section>

    <p class="product__size">6 OZ</p>
  </main>
</body>
</html>
```